Cosmetic Clinic Looking For Sign Designs

We are looking for sign design ideas for the front of our building and a lawn sign for our cosmetic injection salon.
I have uploaded the front of our building for a mock up and size, lawn posts with size and a sign that uses the same dimensions.
We would like both signs to be black for the background.

Target Market(s)

Ages 18-75

Industry/Entity Type

Beauty

Requirements
Must have
• Services we offer:
• Cosmetic Injections
• Airbrush Spray Tanning
• Eyelash Growth Serum
• Skin Care Products & More
• Everything must be on a black background
• The lawn sign must have the address: 394 Fenwick and the building sign should have the phone number.
Should not have
• Nothing can light up (no LED)
• Both signs do not need the full address. Just 394 Fenwick and the phone number

```html
<!DOCTYPE html>
<html lang="en">
<head>
<meta charset="utf-8">
<title>Sunlit Hour Salon – Lawn Sign</title>
<link rel="stylesheet" href="https://fonts.googleapis.com/css2?family=Roboto+Condensed:wght@700&family=Source+Sans+3:wght@400;600&display=swap">
<style>
  :root {
    --sign-black: #000000;
    --brand-teal: #239ab8;
    --accent-pink: #ed1877;
    --mark-lilac: #7b82bf;
    --text-white: #ffffff;
  }
  html, body {
    margin: 0;
    padding: 0;
    width: 1200px;
    height: 1200px;
    overflow: hidden;
    background: var(--sign-black);
  }
  .sign {
    position: relative;
    width: 1200px;
    height: 1200px;
    background: var(--sign-black);
    font-family: "Source Sans 3", "Source Sans Pro", sans-serif;
    color: var(--text-white);
  }
  .sign__rules {
    position: absolute;
    inset: 0;
  }
  .brand-name {
    position: absolute;
    left: 0;
    width: 1200px;
    text-align: center;
    margin: 0;
    font-family: "Roboto Condensed", "Arial Narrow", sans-serif;
    font-weight: 700;
    color: var(--brand-teal);
    line-height: 1;
  }
  .brand-name__main {
    top: 386px;
    font-size: 146px;
    letter-spacing: 2px;
  }
  .brand-name__sub {
    top: 530px;
    font-size: 76px;
    letter-spacing: 3px;
  }
  .services {
    position: absolute;
    top: 793px;
    margin: 0;
    padding: 0;
    list-style: none;
    font-size: 33px;
    line-height: 50px;
    letter-spacing: 1.5px;
    text-transform: uppercase;
    white-space: nowrap;
  }
  .services--left {
    left: 117px;
  }
  .services--right {
    left: 565px;
    width: 600px;
    text-align: center;
  }
  .address {
    position: absolute;
    top: 1060px;
    left: 0;
    width: 1200px;
    margin: 0;
    text-align: center;
    font-size: 57px;
    font-weight: 600;
    letter-spacing: 6px;
    text-transform: uppercase;
  }
</style>
</head>
<body>
  <main class="sign">
    <svg class="sign__rules" width="1200" height="1200" viewBox="0 0 1200 1200" aria-hidden="true">
      <circle class="brand-circle" cx="603" cy="188" r="145" fill="var(--mark-lilac)" stroke="var(--accent-pink)" stroke-width="18"/>
      <polygon class="flank-rule" points="227,562 449,556 449,568" fill="var(--accent-pink)"/>
      <polygon class="flank-rule" points="978,562 757,556 757,568" fill="var(--accent-pink)"/>
      <polygon class="divider-rule" points="106,644 623,642 1141,644 623,646" fill="var(--accent-pink)"/>
      <polygon class="column-divider" points="587,805 588.5,842 587,879 585.5,842" fill="var(--accent-pink)"/>
      <polygon class="divider-rule" points="81,963 600,961 1118,963 600,965" fill="var(--accent-pink)"/>
    </svg>

    <h1 class="brand-name brand-name__main">SUNLIT HOUR</h1>
    <p class="brand-name brand-name__sub">SALON</p>

    <ul class="services services--left">
      <li>Cosmetic Injections</li>
      <li>Eyelash Growth Serum</li>
    </ul>
    <ul class="services services--right">
      <li>Airbrush Spray Tanning</li>
      <li>Skin Care Products &amp; More</li>
    </ul>

    <p class="address">394 Fenwick Street</p>
  </main>
</body>
</html>
```